Complete Re-Design of brentholloway.com

We are looking for a designer/developer that can create a personal branding website design for BrentHolloway.com. The current site is live and operational, but needs a complete redesign to make it more modern, professional, stunning, and to really showcase Brent and his expertise.
We need all the same content and services currently on the site to be migrated over, so keep that in mind when designing the homepage. We want layout, colors, style, and features that will really impress visitors and keep them engaged on the website and ultimately to purchase our services. Ultimately our goal is to gain clients and customers, and to make brent stand out as a trusted expert in his field.
Brent is a domain expert, public speaker, mentor, and coach, a serial entrepreneur and owner of multiple successful online businesses. Please read and review BrentHolloway.com to get a good idea of his background, personality, and what he offers.
An example of a personal branding site that we are impressed with is www.mikefenwright.com, however we do NOT necessarily want to copy his site, just use it as a reference for the level of quality we are looking for. We want lots of ideas and options, you as the designer may have unique and innovative ideas that we havent thought of yet that will blow us away. We want to see your creativity in action.
Number of Pages Required
1 page
Requirements
Must have
- https://www.filevaultz.com/sh/qk372pzrtwnb18xd/KLMtrQWpZnVcRsDxGhJYkLmNa?oref=e
- file vaultz link to photos of Brent you can use.
- Must include the current features and options on our current navigation menu, but they can be featured and showcased in a different better way
- This is for an public figure/expert/entreprenuer who is looking to take his personal brand to the next level, and also redesign his website to reflect that.
- We already have a lot of content and images, and videos from his previous site that would need to be transferred over.
Should not have
- Old outdated colors, fonts, images, style. Nothing too feminine.

```html
<!DOCTYPE html>
<html lang="en">
<head>
<meta charset="utf-8">
<title>Brent Holloway — Domain Expert</title>
<link href="https://fonts.googleapis.com/css2?family=Roboto:wght@400;500;700&display=swap" rel="stylesheet">
<style>
:root{
  --blue:#3d92e8;
  --blue-dark:#2f7fd4;
  --orange:#f5821f;
  --ink:#2b2b2b;
  --ink-soft:#383838;
  --text:#333333;
  --muted:#666666;
  --white:#ffffff;
  --red:#e8312a;
  --field-text:#9a9a9a;
}
*{box-sizing:border-box;margin:0;padding:0}
html,body{width:1200px;height:3090px;overflow:hidden}
body{font-family:'Roboto',Arial,sans-serif;color:var(--text);background:var(--white);position:relative}
.abs{position:absolute}

/* Navigation */
.main-nav{position:absolute;top:0;left:0;width:1200px;height:36px;z-index:5;display:flex;align-items:center;padding-left:10px;gap:20px;font-size:17px;color:var(--white)}
.main-nav .active{background:#4a4a4a;padding:6px 8px;margin:0 -8px}
.main-nav .book-link{background:var(--blue);padding:6px 10px;border-radius:3px;margin-left:130px}
.dropdown{position:absolute;top:36px;left:299px;width:283px;background:var(--ink-soft);z-index:5;padding:6px 10px 8px}
.dropdown li{list-style:none;color:var(--white);font-size:16px;line-height:31px}

/* Hero */
.hero{position:absolute;top:0;left:0;width:1200px;height:675px;background:var(--ink);overflow:hidden}
.hero-bg{position:absolute;inset:0}
.brand{position:absolute;left:77px;top:58px}
.brand-name{font-size:30px;font-weight:700;color:var(--blue)}
.brand-role{font-size:20px;font-weight:700;color:var(--orange);margin-top:2px}
.portrait{position:absolute;left:26px;top:193px;width:347px;height:482px;background:linear-gradient(180deg,#7d8590 0%,#3f4754 55%,#1f2835 100%)}

.booking{position:absolute;left:685px;top:137px;width:422px}
.booking h2{font-size:30px;font-weight:700;color:var(--white)}
.booking .sub{font-size:20px;color:var(--blue);margin-top:6px}
.field{background:var(--white);height:34px;font-size:16px;color:var(--field-text);padding:8px 10px;line-height:18px}
.field.select{color:#222;margin-top:14px}
.field-row{display:flex;gap:14px;margin-top:14px}
.field-row .field{flex:1}
.message{position:relative;margin-top:14px;height:191px;background:var(--white);padding:8px 10px;font-size:16px;color:var(--field-text)}
.message svg{position:absolute;right:0;bottom:-43px}
.btn-book{margin-top:13px;display:inline-block;background:var(--blue);color:var(--white);font-size:17px;padding:8px 10px;border:1px solid #7fb6ef}

/* Services */
.services{position:absolute;top:700px;left:75px;width:1050px;display:grid;grid-template-columns:repeat(4,1fr);text-align:center}
.service{padding:0 30px}
.service h3{font-size:21px;font-weight:700;color:var(--blue)}
.service svg{display:block;margin:12px auto 10px}
.service p{font-size:13.5px;line-height:17px;color:var(--text)}
.service .more{font-size:13px;color:var(--muted);margin-top:2px}
.rule{position:absolute;left:77px;width:1046px;height:2px;background:var(--blue)}

/* Content sections */
.section-title{font-size:31px;color:var(--blue);font-weight:400}
.body-copy{font-size:14px;line-height:17.5px;color:var(--text)}
.body-copy p+p{margin-top:10px}
.body-copy .link{color:var(--blue)}
.body-copy .alert{color:var(--red)}
.btn-primary{display:inline-block;background:var(--blue);color:var(--white);font-size:17px;padding:8px 20px}

.about{left:100px;top:983px;width:510px}
.about .section-title{margin-bottom:12px}
.about .btn-primary{margin-top:14px}
.pet-photo{left:626px;top:979px;width:430px;height:291px;background:linear-gradient(135deg,#cfd6df 0%,#8fa1b5 45%,#c9b08a 70%,#e9e3da 100%)}

.person-photo{left:100px;top:1385px;width:472px;height:475px;background:linear-gradient(160deg,#5c4a3f 0%,#a88a75 45%,#e6ddd5 100%)}
.design-notes{left:626px;top:1390px;width:480px}
.design-notes .section-title{margin-bottom:14px}

.band-blue{left:0;top:1905px;width:1200px;height:168px;background:var(--blue)}
.band-blue .section-title{position:absolute;left:100px;top:50px;color:var(--white)}
.band-blue .body-copy{position:absolute;left:100px;top:98px;width:560px;color:var(--white);font-size:13.5px}
.btn-outline{position:absolute;left:721px;top:52px;width:283px;height:44px;border:2px solid var(--white);border-radius:6px;color:var(--white);font-size:17px;text-align:center;line-height:40px}

.feedback .section-title{position:absolute;left:100px;top:2122px}
.feedback .body-copy{position:absolute;left:626px;top:2128px;width:480px}

.band-dark{left:0;top:2237px;width:1200px;height:480px;background:var(--ink);overflow:hidden}
.band-dark svg{position:absolute;inset:0}
.band-dark .section-title{position:absolute;left:626px;top:48px;color:var(--blue)}
.band-dark .body-copy{position:absolute;left:626px;top:94px;width:500px;color:var(--white)}

.closing .section-title{position:absolute;left:100px;top:2760px}
.closing .body-copy{position:absolute;left:626px;top:2762px;width:480px}

/* Footer */
.site-footer{left:0;top:2846px;width:1200px;height:244px;background:var(--blue);color:var(--white)}
.footer-brand{position:absolute;left:88px;top:36px}
.footer-brand .brand-name{color:var(--white);font-size:25px}
.footer-brand .brand-role{font-size:19px}
.social{position:absolute;left:88px;top:112px;width:230px;display:flex;flex-wrap:wrap;gap:14px 16px;align-items:center;font-size:14px;font-weight:700}
.footer-col{position:absolute;top:40px;font-size:13px;line-height:16px}
.footer-col h4{font-size:20px;font-weight:700;line-height:24px;margin-bottom:2px}
.col-categories{left:350px}
.col-topics{left:615px;top:32px}
.col-media{left:875px;top:32px}
</style>
</head>
<body>

<header class="hero">
  <svg class="hero-bg" width="1200" height="675" viewBox="0 0 1200 675" aria-hidden="true">
    <polygon points="590,0 1200,0 1200,675 340,675" fill="#333333"/>
    <polygon points="1000,0 1200,0 1200,675 860,675" fill="#2f2f2f"/>
  </svg>
  <div class="brand">
    <div class="brand-name">Brent Holloway</div>
    <div class="brand-role">Domain expert</div>
  </div>
  <div class="portrait" role="img" aria-label="Portrait photo of Brent in a dark suit"></div>

  <form class="booking">
    <h2>Book Brent today!</h2>
    <div class="sub">Domain Expert</div>
    <div class="field select">What is it Regarding?</div>
    <div class="field-row"><div class="field">Your Name</div><div class="field">Business Name</div></div>
    <div class="field-row"><div class="field">Your Contact Number</div><div class="field">Your Email Address</div></div>
    <div class="message">Your Message
      <svg width="40" height="44" viewBox="0 0 40 44" aria-hidden="true"><polygon points="0,0 40,0 40,44" fill="#ffffff"/></svg>
    </div>
    <div class="btn-book">Book today!</div>
  </form>
</header>

<nav class="main-nav">
  <span>Home</span><span>About</span><span>News</span><span>Blog</span><span>Press</span>
  <span class="active">Services</span><span>Resources</span>
  <span class="book-link">Book Brent</span>
</nav>
<ul class="dropdown">
  <li>Order a Domain Review</li>
  <li>Order a Premium Domain Review</li>
  <li>Order Private Coaching</li>
  <li>Order a domain Selling Negotation</li>
  <li>Order a Web/Seminar</li>
  <li>Order a Speaking Engagement</li>
  <li>Request an Interview</li>
</ul>

<section class="services">
  <div class="service">
    <h3>Domain expert</h3>
    <svg width="44" height="44" viewBox="0 0 44 44" aria-hidden="true" fill="none" stroke="#3d92e8" stroke-width="2.5">
      <circle cx="22" cy="22" r="19"/><ellipse cx="22" cy="22" rx="8" ry="19"/><line x1="3" y1="22" x2="41" y2="22"/><path d="M6 12h32M6 32h32"/>
    </svg>
    <p>Brent Holloway is the driving force behind NameTalkHub.com, which is one of the most popular domain name forums on the Internet.</p>
    <div class="more">Read More</div>
  </div>
  <div class="service">
    <h3>SEO Specialist</h3>
    <svg width="48" height="48" viewBox="0 0 48 48" aria-hidden="true">
      <circle cx="19" cy="19" r="14" fill="none" stroke="#3d92e8" stroke-width="5"/><line x1="29" y1="29" x2="44" y2="44" stroke="#3d92e8" stroke-width="7" stroke-linecap="round"/>
    </svg>
    <p>We bring a wealth of experience in web development and marketing strategy to every client, whether a large corporate website project or a small business.</p>
    <div class="more">Read More</div>
  </div>
  <div class="service">
    <h3>Web design expert</h3>
    <svg width="48" height="44" viewBox="0 0 48 44" aria-hidden="true">
      <rect x="3" y="3" width="42" height="28" fill="none" stroke="#3d92e8" stroke-width="4"/><rect x="20" y="31" width="8" height="7" fill="#3d92e8"/><rect x="13" y="38" width="22" height="4" fill="#3d92e8"/>
    </svg>
    <p>NicheSiteWorks.com — A web design company that can create a profitable website for $399 in just 3 business days.</p>
    <div class="more">Read More</div>
  </div>
  <div class="service">
    <h3>Public Speaker</h3>
    <svg width="50" height="44" viewBox="0 0 50 44" aria-hidden="true">
      <path d="M2 4h28v18H14l-8 7v-7H2z" fill="#3d92e8"/><path d="M20 18h28v18h-4v7l-8-7H20z" fill="#3d92e8" stroke="#fff" stroke-width="2"/>
    </svg>
    <p>Brent has given more than 5,000 talks and seminars and has worked with more than 1,000 companies worldwide.</p>
    <div class="more">Read More</div>
  </div>
</section>

<div class="rule" style="top:927px"></div>

<section class="abs about">
  <h2 class="section-title">About Brent Holloway</h2>
  <div class="body-copy">
    <p>It's better for SEO now to put a short description in the content of the site rather than just in the meta tags of the header of the document as of 2015 searchly algorithms. <span class="link">More on this here.</span> It's basically done so that there is content in the site and when someone reads the description searchly has it matches the content on the site. Personally I think it looks more professional to add a small description in the index page. You could always add a link to your bigger description :) Like below,</p>
    <p>sorry used the doggie because I thought he was cute</p>
  </div>
  <div class="btn-primary">Read more</div>
</section>
<div class="abs pet-photo" role="img" aria-label="Photo of a small terrier dog sitting on a floor"></div>

<div class="rule" style="top:1331px"></div>

<div class="abs person-photo" role="img" aria-label="Photo of a young woman wearing oversized glasses"></div>
<section class="abs design-notes">
  <h2 class="section-title">About the design</h2>
  <div class="body-copy">
    <p>The design I've supplied you with is what I call "keeping it basic". I haven't over complicated things too far so not to cause issues. Currently I've left it as a +800 res design as I didn't want to do too much for you just to preview the design. This isn't something I've prebuilt, I've made this bespoke so I could change whatever you want. Right now I'm just playing with ideas.</p>
    <p>I've also left out some javascript for a sort of "text slider" I was going to build above the form that fades in and fades out different text that I've listed there.</p>
    <p>I can tell from your site that you're using siteforge. I can build you a raw siteforge theme that will have 'plugins' as people call them built into the template. This way there's no messing about with the plugins.</p>
    <p>The design I think I've kept it clean and neat. But I'm going to throw in a few extra sections below to show you what I think you can alternate with :)</p>
    <p class="alert">For the element #feature, or the header section of the document. I wasn't able to access one of the images with you reading the news paper. I could put that behind everything rather than just your photo.</p>
    <p>Your logo I'm going to build into pure CSS. this way it'll download faster and is accessable by searchly bots.</p>
  </div>
</section>

<section class="abs band-blue">
  <h2 class="section-title">This is alternative</h2>
  <div class="body-copy">This is an alternative section as I call it. Just stands out of the page because of the coloured background. keeping these small looks good I think.</div>
  <div class="btn-outline">alt button</div>
</section>

<section class="feedback">
  <h2 class="section-title">Let me know what you think :)</h2>
  <div class="body-copy">
    <p>I can make any changes you want so let me know and we can work on the design together.</p>
    <p>If you would lik my contact email let me know :)</p>
  </div>
</section>

<section class="abs band-dark">
  <svg width="1200" height="480" viewBox="0 0 1200 480" aria-hidden="true">
    <polygon points="0,0 385,0 670,480 0,480" fill="#333333"/>
  </svg>
  <h2 class="section-title">Another alternative section?</h2>
  <div class="body-copy">You could even add another alternative section like this is show off something. Looks similar to the header but it's in reverse colours. Could even just have an image in the background instead.</div>
</section>

<section class="closing">
  <h2 class="section-title">Back to normal</h2>
  <div class="body-copy">
    <p>You may want to avoid putting alternatives next to your footer as it'll class.</p>
    <p>Or it could provide an extention heading to your footer.</p>
  </div>
</section>

<footer class="abs site-footer">
  <div class="footer-brand">
    <div class="brand-name">Brent Holloway</div>
    <div class="brand-role">Domain expert</div>
  </div>
  <div class="social">
    <span>Friendbook</span>
    <svg width="22" height="22" viewBox="0 0 22 22" aria-label="Feed"><circle cx="4" cy="18" r="3" fill="#fff"/><path d="M2 9a11 11 0 0 1 11 11M2 2a18 18 0 0 1 18 18" fill="none" stroke="#fff" stroke-width="3"/></svg>
    <span>Chirper</span>
    <span>ViewTube</span>
    <span>Circlenet</span>
    <span>Linkfolio</span>
    <svg width="26" height="18" viewBox="0 0 26 18" aria-label="Email"><rect x="1" y="1" width="24" height="16" fill="#fff"/><path d="M1 1l12 9 12-9" fill="none" stroke="#3d92e8" stroke-width="2"/></svg>
  </div>
  <div class="footer-col col-categories">
    <h4>Categories</h4>
    <div>Separating your categories</div>
    <div>Makes them more readable</div>
    <div>Cool siteforge plugins</div>
    <div>NameTalk Forum</div>
  </div>
  <div class="footer-col col-topics">
    <div>Domain Sales</div>
    <div>Domain Software</div>
    <div>Searchly</div>
    <div>ect</div>
  </div>
  <div class="footer-col col-media">
    <div>Sales Videos</div>
    <div>SEO Software</div>
    <div>Web Design</div>
    <div>ect</div>
  </div>
</footer>

</body>
</html>
```